Medical Supply company in need of mail flyers

We are a medical supply company based out of West Palm Beach, Florida. Our website is StrideFreeBoots.Com but we also go by Velorin Medical Supply. We provide shoes through various insurance companies at no cost to the client.We're in need of multiple mail flyers for diabetic footwear customer retention. We will be choosing the top 2 designs submitted.

Industry/Entity Type

Medical Equipment

Requirements
Must have
• Flyers must be 6x9

```html
<!DOCTYPE html>
<html lang="en">
<head>
<meta charset="utf-8">
<title>StrideFree Boots – Diabetic Shoes Flyer</title>
<link href="https://fonts.googleapis.com/css2?family=Fira+Sans+Condensed:wght@600;700&family=Lato:ital,wght@0,400;0,700;0,900;1,700&display=swap" rel="stylesheet">
<style>
  :root{
    --blue:#47719c;
    --green:#7dc471;
    --green-line:#6cbf61;
    --white:#ffffff;
    --photo-a:#8a7a66;
    --photo-b:#5e6f7c;
    --photo-c:#2b2a2c;
    --map-a:#eef1f4;
    --map-b:#d8dee4;
    --map-edge:#2d3a46;
  }
  *{margin:0;padding:0;box-sizing:border-box}
  html,body{width:901px;height:1200px;overflow:hidden;background:var(--white)}
  .flyer{position:absolute;left:0;top:0;width:901px;height:1200px;background:var(--white);overflow:hidden;font-family:"Lato",sans-serif}
  .shapes{position:absolute;left:0;top:0}
  .photo-area{position:absolute;left:0;top:0;width:440px;height:505px}
  .brand{position:absolute;left:493px;top:88px;width:355px;text-align:center;font-weight:900;font-size:44px;line-height:54px;color:var(--blue);letter-spacing:-.5px}
  .headline{position:absolute;left:493px;top:207px;width:355px;text-align:center;font-family:"Fira Sans Condensed",sans-serif;font-weight:700;font-size:45px;line-height:54px;color:var(--blue);text-transform:uppercase}
  .coverage-note{position:absolute;left:40px;top:554px;width:436px;text-align:center;color:var(--white);font-style:italic;font-weight:700;font-size:17px;line-height:22.5px}
  .about-title{position:absolute;left:45px;top:676px;color:var(--white);font-weight:700;font-size:21px;line-height:26px}
  .about-text{position:absolute;left:45px;top:709px;width:428px;color:var(--white);font-size:13px;line-height:17.2px;text-align:justify}
  .shoe-lineup{position:absolute;left:45px;top:852px;width:440px;height:80px;border-radius:40px;background:linear-gradient(90deg,#6f7378,#8a5a3e,#2f2f33,#55585c)}
  .social{position:absolute;top:955px;width:50px;height:50px;border:3px solid var(--white);border-radius:50%}
  .contact{position:absolute;left:30px;width:470px;text-align:center;color:var(--white);font-weight:700;font-size:27px;line-height:30px}
  .steps-title{position:absolute;left:493px;top:482px;width:356px;text-align:center;color:var(--white);font-weight:700;font-size:20px;line-height:28px}
  .step-caption{position:absolute;width:170px;text-align:center;color:var(--white);font-size:11.5px;line-height:14px}
  .map{position:absolute;left:504px;top:850px;width:334px;height:334px;border-radius:50%;background:radial-gradient(circle at 45% 40%,var(--map-a),var(--map-b));border:5px solid var(--map-edge)}
  .address{position:absolute;left:20px;top:1124px;width:470px;text-align:center;color:var(--green-line);font-weight:700;font-size:22px;line-height:28px}
</style>
</head>
<body>
<main class="flyer">
  <svg class="shapes" width="901" height="1200" viewBox="0 0 901 1200" aria-hidden="true">
    <defs>
      <clipPath id="photoClip"><circle cx="190" cy="253" r="245"/></clipPath>
      <linearGradient id="photoGrad" x1="0" y1="0" x2="0" y2="1">
        <stop offset="0" stop-color="var(--photo-b)"/>
        <stop offset=".55" stop-color="var(--photo-c)"/>
        <stop offset="1" stop-color="var(--photo-a)"/>
      </linearGradient>
    </defs>
    <path d="M0 530 Q260 470 560 560 Q760 620 901 575 L901 1200 L0 1200 Z" fill="var(--green)"/>
    <path d="M0 512 Q260 452 560 542 Q760 602 901 557 L901 590 Q760 636 560 578 Q260 488 0 545 Z" fill="var(--blue)"/>
    <circle cx="190" cy="253" r="262" fill="var(--white)"/>
    <circle cx="190" cy="253" r="256" fill="none" stroke="var(--blue)" stroke-width="8"/>
    <circle cx="190" cy="253" r="248" fill="none" stroke="var(--green)" stroke-width="5"/>
    <g clip-path="url(#photoClip)">
      <rect x="-60" y="0" width="520" height="500" fill="url(#photoGrad)"/>
    </g>
    <path d="M520 450 L849 450 L849 1200 L493 1200 L493 477 Q493 450 520 450 Z" fill="var(--blue)"/>
    <rect x="494" y="162" width="354" height="5" fill="var(--green-line)"/>
    <path d="M656 166 L686 166 L671 181 Z" fill="var(--green-line)"/>
    <g fill="var(--green)" stroke="var(--white)" stroke-width="3">
      <circle cx="582" cy="609" r="39"/>
      <circle cx="761" cy="609" r="39"/>
      <circle cx="582" cy="745" r="39"/>
      <circle cx="761" cy="745" r="39"/>
    </g>
    <g fill="var(--white)">
      <circle cx="643" cy="609" r="2.5"/><circle cx="653" cy="609" r="3.5"/><circle cx="665" cy="609" r="4.5"/><circle cx="679" cy="609" r="5"/>
      <circle cx="653" cy="745" r="2.5"/><circle cx="663" cy="745" r="3.5"/><circle cx="675" cy="745" r="4.5"/><circle cx="689" cy="745" r="5"/>
    </g>
    <g fill="none" stroke="var(--white)" stroke-width="2.5">
      <path d="M568 589 L590 589 L598 597 L598 629 L568 629 Z"/>
      <path d="M574 604 H592 M574 611 H592 M574 618 H592"/>
      <rect x="746" y="592" width="28" height="36" rx="2"/>
      <rect x="754" y="588" width="12" height="7" rx="2"/>
      <path d="M752 606 H768 M752 613 H768 M752 620 H764"/>
      <path d="M562 755 Q564 738 576 738 L588 746 Q598 750 604 756 L604 760 L562 760 Z"/>
      <circle cx="747" cy="730" r="4"/><path d="M747 736 V760"/>
      <circle cx="775" cy="730" r="4"/><path d="M775 736 V760"/>
      <rect x="755" y="740" width="12" height="9"/>
    </g>
    <path d="M0 1108 Q230 1080 500 1100 Q740 1118 901 1186 L901 1200 L0 1200 Z" fill="var(--blue)"/>
    <path d="M0 1116 Q230 1090 500 1110 Q740 1128 901 1196 L901 1200 L0 1200 Z" fill="var(--white)"/>
  </svg>
  <div class="photo-area" role="img" aria-label="Photo of black and brown leather diabetic shoes on a wooden dock"></div>

  <div class="brand">StrideFree Boots</div>
  <h1 class="headline">Diabetic Shoes<br>or Sneakers<br>Covered<br>by Medicare</h1>

  <p class="coverage-note">No or little out of pocket Cost To You!*<br>Medicare, and most insurance plans, may cover the<br>cost of one pair of diabetic shoes and three pairs<br>of custom inserts per calendar year. Co-payments,<br>deductibles and some restrictions apply.</p>

  <h2 class="about-title">ABOUT US</h2>
  <p class="about-text">StrideFreeBoots.Com was created by Velorin Medical Supply to educate clients and prospective shoe fitters about diabetic shoes and the coverage that Medicare provides. Founded by a Board-Certified Pedorthist, the company's mission is to help clients receive properly fitted shoes from qualified healthcare professionals around the United States. Velorin Medical Supply works directly with Medicare to determine the patient's coverage.</p>

  <div class="shoe-lineup" role="img" aria-label="Row of four diabetic shoes: grey sneaker, brown leather lace-up, black strap shoe and black walking shoe"></div>

  <span class="social" style="left:152px"></span>
  <span class="social" style="left:211px"></span>
  <span class="social" style="left:270px"></span>
  <span class="social" style="left:328px"></span>

  <p class="contact" style="top:1020px">Ph: 1-866-555-0142</p>
  <p class="contact" style="top:1050px">E: orders@stridefreeboots.com</p>

  <h2 class="steps-title">4 Easy Steps To Receive<br>Your New Therapeutic Shoes.</h2>
  <p class="step-caption" style="left:497px;top:662px">Fill out an application to see<br>if your qualify</p>
  <p class="step-caption" style="left:676px;top:662px">A prescription will be faxed<br>to your primary physician.</p>
  <p class="step-caption" style="left:497px;top:795px">After the prescription is<br>signed, a certified shoe fitter<br>will fit your new shoes.</p>
  <p class="step-caption" style="left:676px;top:795px">Enjoy your new shoes!</p>

  <div class="map" role="img" aria-label="Street map showing the office location"></div>

  <p class="address">Velorin Medical : 2740 Harbor Palm<br>Ave Ste 410 Coral Vista, Fl 33999</p>
</main>
</body>
</html>
```